Label Redesign For Hemp Oil Tincture Bottle*

I need a label redesigned for Marbleleaf Hemp, current bottle label and logo is attached. The current label doesn't standout, not sure if its the font size or colors on the existing label. It is very important to have on the label that this is a Premium Full Spectrum Hemp Oil that is 2000mg. Then after the label is redesigned and approved, I would need to packaging to be designed to match the approved label design.
This Hemp oil has a relaxing effect to help ease mental and emotional stress, tension and worry. The Omega Fatty Acids it contains also naturally improves your mood and overall brain function, causing you to feel more alert and focused. Hemp Oil helps with insomnia. Take some 2-3 hours before bedtime, you will feel relaxed yet aware of how tired you are that it will lead to a good night's sleep. Hemp Oil helps ease chronic pain and inflammation from conditions such as arthritis, fibromyalgia, lupus, and MS. As a pain relief supplement, it is a safer, natural, non-chemical and non-addictive alternative to prescription painkillers.

Target Market(s)

Adults

Industry/Entity Type

Supplement

Font styles to use
Serif
Sans Serif

Colors

Designer to choose colors to be used in the design.

Requirements
Must have
• All information thats on current label but where it says 750 in the front of the existing label, it needs to say 2000. The 2000 should be prominent on the label.

```html
<!DOCTYPE html>
<html lang="en">
<head>
<meta charset="utf-8">
<title>Marbleleaf Hemp – Full Spectrum Hemp Oil Label</title>
<link rel="stylesheet" href="https://fonts.googleapis.com/css2?family=Oranienbaum&family=Rosarivo&display=swap">
<style>
  :root {
    --page-bg: #f2f4ee;
    --label-light: #79bf34;
    --label-mid: #63a923;
    --label-deep: #4f9418;
    --panel-green: #22701a;
    --panel-frame: #0f4a0c;
    --pill-green: #174a10;
    --pill-edge: #9fd36a;
    --ink-dark: #0c1a08;
    --ink-light: #ffffff;
  }
  * { margin: 0; padding: 0; box-sizing: border-box; }
  html, body {
    width: 891px; height: 1200px; overflow: hidden;
    background: var(--page-bg);
  }
  .canvas {
    position: relative; width: 891px; height: 1200px;
  }
  .label {
    position: absolute; left: 85px; top: 25px;
    width: 721px; height: 1150px;
    font-family: "Oranienbaum", "Times New Roman", serif;
    color: var(--ink-dark);
    text-align: center;
    overflow: hidden;
  }
  .label-pattern {
    position: absolute; inset: 0;
    background:
      radial-gradient(ellipse at 50% 40%, var(--label-light) 0%, var(--label-mid) 60%, var(--label-deep) 100%);
  }
  .brand-mark {
    position: absolute; left: 0; right: 0; top: 95px;
    display: flex; align-items: center; justify-content: center; gap: 14px;
    font-size: 34px; color: var(--ink-dark);
  }
  .brand-mark .dot {
    width: 22px; height: 22px; border-radius: 50%;
    background: var(--pill-green);
  }
  .thc-pill {
    position: absolute; left: 246px; top: 252px;
    width: 229px; height: 80px; border-radius: 40px;
    background: var(--pill-green);
    border: 3px solid var(--pill-edge);
    color: #b9e58c;
    font-size: 42px; line-height: 74px;
  }
  .brand-title {
    position: absolute; left: 0; right: 0; top: 362px;
    font-size: 92px; line-height: 110px; letter-spacing: -1px;
  }
  .product-panel {
    position: absolute; left: 108px; top: 499px;
    width: 505px; height: 353px;
  }
  .product-panel svg { position: absolute; inset: 0; }
  .product-panel .lines {
    position: absolute; left: 0; right: 0; top: 22px;
    color: var(--ink-light);
  }
  .product-panel .line {
    font-size: 66px; line-height: 80px;
  }
  .product-panel .strength {
    font-family: "Rosarivo", "Times New Roman", serif;
    font-size: 64px; font-weight: 400; letter-spacing: 1px;
  }
  .dose {
    position: absolute; left: 0; right: 0; top: 876px;
    font-family: "Rosarivo", "Times New Roman", serif;
    font-size: 68px; line-height: 80px; letter-spacing: -1px;
  }
  .supplement-type {
    position: absolute; left: 0; right: 0; top: 962px;
    font-size: 26px; letter-spacing: 0;
  }
  .volume {
    position: absolute; left: 0; right: 0; top: 1012px;
    font-size: 26px;
  }
  .flavor {
    position: absolute; left: 0; right: 0; top: 1068px;
    font-size: 37px;
  }
</style>
</head>
<body>
<div class="canvas">
  <section class="label">
    <div class="label-pattern" role="img" aria-label="Green label background with a fine leaf and flower line pattern"></div>

    <div class="brand-mark"><span class="dot"></span><span>Marbleleaf Hemp</span></div>

    <div class="thc-pill">Zero THC</div>

    <h1 class="brand-title">Marbleleaf Hemp</h1>

    <div class="product-panel">
      <svg width="505" height="353" viewBox="0 0 505 353" aria-hidden="true">
        <rect x="8" y="8" width="489" height="337" fill="#22701a"/>
        <rect x="2" y="2" width="501" height="349" fill="none" stroke="#0f4a0c" stroke-width="3"/>
        <rect x="14" y="14" width="477" height="325" fill="none" stroke="#0f4a0c" stroke-width="2"/>
      </svg>
      <div class="lines">
        <div class="line">Premium</div>
        <div class="line">Full Spectrum</div>
        <div class="line strength">2000</div>
        <div class="line">Hemp Oil</div>
      </div>
    </div>

    <div class="dose">2000 mg</div>
    <div class="supplement-type">DIETARY SUPPLEMENTS</div>
    <div class="volume">1 FL OZ (30ML)</div>
    <div class="flavor">Natural Peppermint Flavor</div>
  </section>
</div>
</body>
</html>
```